Concise,Good colour matching,Good looks design for "HERD SURE RAPID TEST FOR LIVESTOCK"

Product Positioning: Affordable test for Large Animals (Livestock/Veterinary Use)
Product Name: HERD SURE Rapid Test Kit (for large animals, e.g., cattle, horses, swine,Avian,sheep).

2. Packaging Requirements

A. Visual Design
Color Scheme:
Green/Blue/Orange/Yellow/Red/Gray/White(chose 2~4 colors)

Mandatory Info:
Brand logo ("HERD SURE")

Target Market(s)

Southeast Asia, Africa, Middle East, South America

Industry/Entity Type

Veterinary diagnostic for LIVESTOCK

Colors

Designer to choose colors to be used in the design.

Requirements
Nice to have
• Concise,Good colour matching,Good looks

```html
<!DOCTYPE html>
<html lang="en">
<head>
<meta charset="utf-8">
<title>HERD SURE Rapid Test Kit – Packaging</title>
<link rel="stylesheet" href="https://fonts.googleapis.com/css2?family=Montserrat:wght@500;600;700;800&display=swap">
<style>
  :root{
    --navy:#1d2f6b;
    --navy-deep:#142253;
    --green:#7ab63f;
    --green-dark:#4f8f2a;
    --orange:#f08a1c;
    --white:#ffffff;
    --cut:#e0457b;
    --paper:#f4f5f7;
  }
  *{margin:0;padding:0;box-sizing:border-box}
  html,body{width:727px;height:1200px;overflow:hidden;background:var(--paper);font-family:"Montserrat",sans-serif}
  .canvas{position:relative;width:727px;height:1200px}
  .dieline{position:absolute;left:0;top:20px;width:727px;height:497px}
  .front-face{position:absolute;left:84px;top:640px;width:560px;height:340px;background:var(--white);overflow:hidden;box-shadow:0 2px 10px rgba(0,0,0,.08)}
  .front-face svg{position:absolute;inset:0}
  .front-title{position:absolute;left:0;right:0;top:72px;text-align:center;font-weight:800;font-size:56px;letter-spacing:2px;line-height:1;color:var(--navy)}
  .front-tagline{position:absolute;left:0;right:0;top:140px;text-align:center;color:var(--green-dark);font-weight:700;font-size:13px;letter-spacing:1.4px}
  .front-brand{position:absolute;left:34px;bottom:34px;color:var(--white);font-weight:800;font-size:17px;letter-spacing:2px;display:flex;align-items:center;gap:8px}
  .front-brand .dot{width:12px;height:12px;border-radius:50%;background:var(--white)}
  .front-badge{position:absolute;right:34px;bottom:26px;width:86px;height:86px;border-radius:50%;background:var(--orange);border:3px solid var(--white);color:var(--white);display:flex;flex-direction:column;align-items:center;justify-content:center;text-align:center;font-weight:800;font-size:10px;line-height:1.25}
  .front-badge strong{font-size:13px}
</style>
</head>
<body>
<main class="canvas">

  <svg class="dieline" viewBox="0 15 300 205" xmlns="http://www.w3.org/2000/svg" font-family="Montserrat, sans-serif">
    <!-- tuck flap -->
    <path d="M100 30 Q100 20 112 20 L188 20 Q200 20 200 30 Z" fill="var(--white)" stroke="var(--cut)" stroke-width=".4"/>

    <!-- lid panel -->
    <g class="lid-panel">
      <rect x="95" y="30" width="110" height="46" fill="var(--white)" stroke="var(--cut)" stroke-width=".4"/>
      <text x="150" y="42" text-anchor="middle" font-weight="800" font-size="8" fill="var(--navy)" letter-spacing=".3">HERD SURE</text>
      <text x="150" y="46.5" text-anchor="middle" font-weight="700" font-size="2.3" fill="var(--green-dark)" letter-spacing=".2">RAPID LIVESTOCK SCREENING FOR EVERY FARM</text>
      <rect x="106" y="51" width="72" height="8" rx="1" fill="var(--navy)" opacity=".8" role="img" aria-label="Row of livestock silhouettes: cattle, horse, pig, poultry, sheep"/>
      <rect x="181" y="50.5" width="19" height="9" fill="var(--navy)"/>
      <text x="190.5" y="54.3" text-anchor="middle" font-weight="800" font-size="2.4" fill="var(--white)">LARGE</text>
      <text x="190.5" y="57.6" text-anchor="middle" font-weight="800" font-size="2.4" fill="var(--white)">ANIMAL</text>
      <path d="M95 66 L205 62 L205 76 L95 76 Z" fill="var(--green)"/>
      <path d="M95 70 L160 76 L95 76 Z" fill="var(--navy)"/>
    </g>

    <!-- dust flaps -->
    <path d="M95 82 L78 86 L78 116 L95 120 Z" fill="var(--white)" stroke="var(--cut)" stroke-width=".4"/>
    <path d="M205 82 L222 86 L222 116 L205 120 Z" fill="var(--white)" stroke="var(--cut)" stroke-width=".4"/>

    <!-- front panel -->
    <g class="front-panel">
      <rect x="95" y="76" width="110" height="44" fill="var(--white)" stroke="var(--cut)" stroke-width=".4"/>
      <path d="M95 76 L118 76 L95 88 Z" fill="var(--navy)"/>
      <text x="150" y="95" text-anchor="middle" font-weight="800" font-size="8" fill="var(--navy)" letter-spacing=".3">HERD SURE</text>
      <text x="150" y="99.5" text-anchor="middle" font-weight="700" font-size="2.3" fill="var(--green-dark)" letter-spacing=".2">RAPID LIVESTOCK SCREENING FOR EVERY FARM</text>
      <path d="M95 110 L205 104 L205 120 L95 120 Z" fill="var(--green)"/>
      <path d="M95 113 L175 120 L95 120 Z" fill="var(--navy)"/>
      <text x="100" y="118" font-weight="800" font-size="2.6" fill="var(--white)" letter-spacing=".3">AGROVA LABS</text>
      <circle cx="192" cy="110" r="8" fill="var(--orange)" stroke="var(--white)" stroke-width=".6"/>
      <text x="192" y="108" text-anchor="middle" font-weight="800" font-size="1.7" fill="var(--white)">RAPID</text>
      <text x="192" y="110.4" text-anchor="middle" font-weight="800" font-size="1.7" fill="var(--white)">RESULTS IN</text>
      <text x="192" y="112.8" text-anchor="middle" font-weight="800" font-size="1.7" fill="var(--white)">10 MINUTES</text>
    </g>

    <!-- middle row -->
    <g class="side-row">
      <rect x="18" y="120" width="34" height="40" fill="var(--navy)" stroke="var(--cut)" stroke-width=".4"/>
      <rect x="52" y="120" width="43" height="40" fill="var(--navy)" stroke="var(--cut)" stroke-width=".4"/>
      <text transform="translate(30 140) rotate(-90)" text-anchor="middle" font-weight="800" font-size="5" fill="var(--white)">HERD SURE</text>
      <text transform="translate(36 140) rotate(-90)" text-anchor="middle" font-weight="600" font-size="1.8" fill="var(--white)">FOR VETERINARY USE ONLY</text>
      <text transform="translate(74 140) rotate(-90)" text-anchor="middle" font-weight="600" font-size="1.8" fill="var(--white)">10 TESTS PER KIT</text>
      <rect x="95" y="120" width="110" height="40" fill="var(--navy-deep)" stroke="var(--cut)" stroke-width=".4"/>
      <rect x="205" y="120" width="24" height="40" fill="var(--white)" stroke="var(--cut)" stroke-width=".4"/>
      <rect x="216" y="120" width="6" height="40" fill="var(--green)"/>
      <text transform="translate(212 140) rotate(90)" text-anchor="middle" font-weight="600" font-size="1.8" fill="var(--navy)">STORE AT 2–30°C</text>
      <rect x="229" y="120" width="53" height="40" fill="var(--navy)" stroke="var(--cut)" stroke-width=".4"/>
      <rect x="262" y="120" width="8" height="40" fill="var(--green)"/>
      <text transform="translate(276 140) rotate(90)" text-anchor="middle" font-weight="800" font-size="5" fill="var(--white)">HERD SURE</text>
    </g>

    <!-- bottom panel (reversed) -->
    <g class="base-panel" transform="rotate(180 150 182.5)">
      <rect x="95" y="160" width="110" height="45" fill="var(--white)" stroke="var(--cut)" stroke-width=".4"/>
      <path d="M95 160 L118 160 L95 172 Z" fill="var(--navy)"/>
      <text x="150" y="180" text-anchor="middle" font-weight="800" font-size="8" fill="var(--navy)" letter-spacing=".3">HERD SURE</text>
      <text x="150" y="184.5" text-anchor="middle" font-weight="700" font-size="2.3" fill="var(--green-dark)" letter-spacing=".2">RAPID LIVESTOCK SCREENING FOR EVERY FARM</text>
      <path d="M95 195 L205 189 L205 205 L95 205 Z" fill="var(--green)"/>
      <path d="M95 198 L175 205 L95 205 Z" fill="var(--navy)"/>
      <text x="100" y="203" font-weight="800" font-size="2.6" fill="var(--white)" letter-spacing=".3">AGROVA LABS</text>
      <circle cx="192" cy="195" r="8" fill="var(--orange)" stroke="var(--white)" stroke-width=".6"/>
      <text x="192" y="193" text-anchor="middle" font-weight="800" font-size="1.7" fill="var(--white)">RAPID</text>
      <text x="192" y="195.4" text-anchor="middle" font-weight="800" font-size="1.7" fill="var(--white)">RESULTS IN</text>
      <text x="192" y="197.8" text-anchor="middle" font-weight="800" font-size="1.7" fill="var(--white)">10 MINUTES</text>
    </g>
    <path d="M95 205 L78 201 L78 168 L95 164 Z" fill="var(--white)" stroke="var(--cut)" stroke-width=".4"/>
    <path d="M205 205 L222 201 L222 168 L205 164 Z" fill="var(--white)" stroke="var(--cut)" stroke-width=".4"/>
  </svg>

  <section class="front-face" aria-label="Box front panel">
    <svg viewBox="0 0 560 340" preserveAspectRatio="none" xmlns="http://www.w3.org/2000/svg">
      <path d="M0 0 L120 0 L0 62 Z" fill="var(--navy)"/>
      <path d="M0 258 L560 218 L560 340 L0 340 Z" fill="var(--green)"/>
      <path d="M0 272 L420 340 L0 340 Z" fill="var(--navy)"/>
    </svg>
    <h1 class="front-title">HERD SURE</h1>
    <p class="front-tagline">RAPID LIVESTOCK SCREENING FOR EVERY FARM</p>
    <div class="front-brand"><span class="dot"></span>AGROVA LABS</div>
    <div class="front-badge"><span>RAPID RESULTS</span><strong>IN 10</strong><span>MINUTES</span></div>
  </section>

</main>
</body>
</html>
```